Start up business website

IT Support provider that caters towards law enforcement / police departments. We'll offer remote IT support, backup / recovery services and cyber security. Will add updates soon.

Target Market(s)

Police departments / Law Enforcement

Coding

Coded - Design and coding required

Number of Pages Required

5+ page

Other font styles liked:
• Use font style in uploaded logo

Colors
0054AA
0677BA
7BADD7
CADEEF
E8F1F8

```html
<!DOCTYPE html>
<html lang="en">
<head>
<meta charset="utf-8">
<title>Bastion Support Services</title>
<link href="https://fonts.googleapis.com/css2?family=Roboto:wght@400;500;700;900&display=swap" rel="stylesheet">
<style>
:root{
  --blue:#0a3aa8;
  --blue-deep:#0b2f8f;
  --blue-band:#1243a8;
  --ink:#1b1b1b;
  --text:#333;
  --muted:#6a6a6a;
  --white:#fff;
  --footer:#050505;
  --line:#e4e4e4;
}
*{margin:0;padding:0;box-sizing:border-box}
html,body{width:1200px;height:3455px;overflow:hidden}
body{position:relative;font-family:'Roboto',Arial,sans-serif;color:var(--text);background:var(--white)}
.abs{position:absolute}
a{color:inherit;text-decoration:none}

/* header */
.site-header{position:absolute;left:0;top:0;width:1200px;height:86px;background:var(--white)}
.brand{position:absolute;left:111px;top:22px;display:flex;align-items:center;gap:8px}
.brand-dot{width:40px;height:40px;border-radius:50%;background:var(--blue)}
.brand-name{font-weight:900;font-size:22px;color:var(--blue);letter-spacing:.5px}
.nav{position:absolute;top:32px;font-size:16px;font-weight:500;color:#222;text-transform:uppercase}
.nav.active{color:var(--blue);border-bottom:2px solid var(--blue);padding-bottom:2px}
.search-icon{position:absolute;left:909px;top:34px}
.btn-login{position:absolute;left:975px;top:23px;width:112px;height:40px;background:var(--blue);color:#fff;font-weight:700;font-size:16px;display:flex;align-items:center;justify-content:center;gap:8px;border-radius:2px}

/* hero */
.hero{position:absolute;left:0;top:86px;width:1200px;height:650px}
.hero-title{position:absolute;left:108px;top:285px;font-size:76px;font-weight:900;color:#fff;letter-spacing:1px}
.hero-sub{position:absolute;left:111px;top:380px;width:400px;font-size:17.5px;line-height:27px;color:#fff}
.btn{display:flex;align-items:center;justify-content:center;gap:10px;font-weight:700;font-size:16px;color:#fff;background:var(--blue);text-transform:uppercase;border-radius:2px}
.hero-btn{position:absolute;left:111px;top:458px;width:169px;height:49px}
.hero-arrow{position:absolute;width:40px;height:40px;border-radius:50%;background:#fff;display:flex;align-items:center;justify-content:center}

/* section titles */
.section-title{position:absolute;left:0;width:1200px;text-align:center;font-size:40px;font-weight:700;color:var(--ink)}
.section-title::after{content:"";display:block;width:48px;height:3px;background:var(--blue);margin:4px auto 0}
.section-title.light{color:#fff}
.section-title.light::after{background:#fff}

/* about */
.about-mark{position:absolute;left:141px;top:820px;width:320px;height:371px;display:flex;align-items:center;justify-content:center;gap:12px}
.about-mark .brand-dot{width:60px;height:60px}
.about-mark span{font-weight:900;font-size:34px;color:var(--blue)}
.about-title{position:absolute;left:519px;top:815px;font-size:40px;font-weight:700;color:var(--ink)}
.about-title::after{content:"";display:block;width:48px;height:3px;background:var(--blue);margin-top:2px}
.about-text{position:absolute;left:519px;top:888px;width:540px;font-size:15.5px;line-height:25.8px;color:#2a2a2a}
.about-btn{position:absolute;left:519px;top:1141px;width:166px;height:48px}

/* services */
.services-band{position:absolute;left:0;top:1284px;width:1200px;height:553px;background:linear-gradient(180deg,#1647b0,#0f3c9e)}
.service-card{position:absolute;top:1435px;width:285px;height:337px;background:#fff;text-align:center}
.service-photo{height:154px}
.service-badge{position:absolute;left:112px;top:116px;width:62px;height:70px;border-radius:50% 50% 50% 50% / 40% 40% 60% 60%;background:var(--blue);border:3px solid #fff;display:flex;align-items:center;justify-content:center}
.service-name{margin-top:52px;font-size:15.5px;font-weight:700;color:#222}
.service-text{margin-top:14px;font-size:15.5px;line-height:23px;color:#444;padding:0 18px}
.read-more{display:inline-flex;align-items:center;gap:8px;margin-top:12px;font-size:15.5px;font-weight:700;color:var(--blue);text-decoration:underline}

/* blogs */
.blog-photo{position:absolute;top:2006px;width:452px;height:293px}
.blog-card{position:absolute;top:2246px;width:402px;height:174px;background:#fff;border-left:8px solid var(--blue);border-bottom:8px solid var(--blue);padding:18px 0 0 24px}
.blog-name{font-size:15.5px;font-weight:700;color:#222}
.blog-meta{margin-top:8px;font-size:13px;color:var(--muted)}
.blog-meta b{font-weight:700}
.blog-text{margin-top:10px;font-size:15.5px;line-height:23px;color:#333;width:365px}

/* contact */
.contact-band{position:absolute;left:0;top:2505px;width:1200px;height:570px;background:linear-gradient(180deg,#1546ad,#0e3a9c)}
.field{position:absolute;background:#fff;border:1px solid #d8d8d8;border-radius:2px;font-size:13px;color:#333;padding:9px 13px}
.btn-submit{position:absolute;left:527px;top:2876px;width:145px;height:48px;border:2px solid #fff;border-radius:3px;display:flex;align-items:center;justify-content:center;gap:10px;color:#fff;font-weight:700;font-size:16px}

/* footer */
.site-footer{position:absolute;left:0;top:3000px;width:1200px;height:455px}
.footer-brand{position:absolute;left:111px;top:3113px;display:flex;align-items:center;gap:10px}
.footer-brand .brand-dot{width:62px;height:62px}
.footer-brand .brand-name{font-size:26px}
.footer-about{position:absolute;left:111px;top:3198px;width:270px;font-size:15.5px;line-height:26px;color:#fff}
.footer-head{position:absolute;font-size:16px;font-weight:700;color:#fff;text-transform:uppercase}
.footer-head::after{content:"";display:block;width:38px;height:2px;background:#fff;margin-top:12px}
.social{position:absolute;top:3325px;width:30px;height:30px;border-radius:50%;border:1.5px solid #fff}
.footer-link{position:absolute;font-size:15.5px;color:#fff}
.footer-link::before{content:"»";margin-right:11px}
.contact-icon{position:absolute;left:881px;width:34px;height:34px;border-radius:50%;background:#fff;display:flex;align-items:center;justify-content:center}
.contact-label{position:absolute;left:931px;font-size:13px;font-weight:700;color:#fff}
.contact-value{position:absolute;left:931px;font-size:15px;line-height:23px;color:#fff}
.footer-rule{position:absolute;left:111px;top:3399px;width:975px;height:1px;background:#333}
.copyright{position:absolute;left:0;top:3417px;width:1200px;text-align:center;font-size:14.5px;color:#fff}
</style>
</head>
<body>

<header class="site-header">
  <div class="brand"><span class="brand-dot"></span><span class="brand-name">BASTION</span></div>
  <a class="nav active" style="left:333px">Home</a>
  <a class="nav" style="left:422px">About Us</a>
  <a class="nav" style="left:546px">Services</a>
  <a class="nav" style="left:669px">Blog</a>
  <a class="nav" style="left:756px">Contact Us</a>
  <svg class="search-icon" width="16" height="16" viewBox="0 0 16 16"><circle cx="6.5" cy="6.5" r="4.5" fill="none" stroke="#222" stroke-width="2"/><line x1="10" y1="10" x2="14" y2="14" stroke="#222" stroke-width="2.4" stroke-linecap="round"/></svg>
  <a class="btn-login">LOGIN
    <svg width="16" height="14" viewBox="0 0 16 14"><path d="M1 5h7V2l5 5-5 5V9H1z" fill="#fff"/><path d="M10 1h4v12h-4" fill="none" stroke="#fff" stroke-width="2"/></svg>
  </a>
</header>

<section class="hero">
  <svg class="abs" style="left:0;top:0" width="1200" height="650" viewBox="0 0 1200 650">
    <defs>
      <linearGradient id="heroFill" x1="0" y1="0" x2="1" y2="0.4">
        <stop offset="0" stop-color="#1c2733"/>
        <stop offset="0.45" stop-color="#3b4a5a"/>
        <stop offset="0.75" stop-color="#5d6b78"/>
        <stop offset="1" stop-color="#2a3440"/>
      </linearGradient>
    </defs>
    <path role="img" aria-label="Photo of two IT technicians talking in a server room" d="M0 0H1200V578L600 648L0 578Z" fill="url(#heroFill)"/>
    <path d="M0 578L600 648L1200 578" fill="none" stroke="var(--blue)" stroke-width="5"/>
  </svg>
  <h1 class="hero-title" style="top:199px">BASTION</h1>
  <p class="hero-sub" style="top:294px">We are a managed service provider that caters towards law enforcement / police departments.</p>
  <a class="btn hero-btn" style="top:372px">Get Started
    <svg width="15" height="15" viewBox="0 0 16 16"><circle cx="8" cy="8" r="8" fill="#fff"/><path d="M6 4l4 4-4 4" fill="none" stroke="var(--blue)" stroke-width="2.2"/></svg>
  </a>
  <span class="hero-arrow" style="left:35px;top:299px"><svg width="12" height="14" viewBox="0 0 12 14"><path d="M8 1L2 7l6 6" fill="none" stroke="#111" stroke-width="2"/></svg></span>
  <span class="hero-arrow" style="left:1124px;top:299px"><svg width="12" height="14" viewBox="0 0 12 14"><path d="M4 1l6 6-6 6" fill="none" stroke="#111" stroke-width="2"/></svg></span>
</section>

<section class="about">
  <div class="about-mark"><span class="brand-dot"></span><span>BASTION</span></div>
  <h2 class="about-title">ABOUT US</h2>
  <p class="about-text">Lorem ipsum dolor sit amet, consectetur adipiscing elit, sed &nbsp;eiusmod tempor incididunt ut labore et dolore magna aliqua. Ut enim ad minim veniam, quis nostrud exercitation ullamco laboris nisi ut aliquip ex ea commodo consequat. Duis aute irure dolor in reprehenderit in voluptate velit esse cillum dolore eu fugiat nulla pariatur. Excepteur sint occaecat cupidatat non proident, sunt in culpa qui officia deserunt mollit anim id est perspiciatis unde omnis iste natus error sit voluptatem accusantium doloremque laudantium laborum.et quasi architecto beatae vitae dicta sunt explicabo. Nemo enim ipsam voluptatem quia voluptas sit.Lorem ipsum dolor sit amet, consectetur adipiscing elit sed</p>
  <a class="btn about-btn">Learn More
    <svg width="15" height="15" viewBox="0 0 16 16"><circle cx="8" cy="8" r="8" fill="#fff"/><path d="M6 4l4 4-4 4" fill="none" stroke="var(--blue)" stroke-width="2.2"/></svg>
  </a>
</section>

<section class="services">
  <div class="services-band"></div>
  <h2 class="section-title light" style="top:1336px">OUR SERVICES</h2>

  <article class="service-card" style="left:139px">
    <div class="service-photo" role="img" aria-label="Photo of a team meeting around a laptop" style="background:linear-gradient(135deg,#c9c4bc,#7d6a5c)"></div>
    <span class="service-badge"><svg width="26" height="26" viewBox="0 0 26 26"><rect x="4" y="6" width="18" height="14" rx="2" fill="none" stroke="#fff" stroke-width="2"/><path d="M8 13l3 3 6-6" fill="none" stroke="#fff" stroke-width="2"/></svg></span>
    <h3 class="service-name">LOREM IPSUM DOLOR SIT</h3>
    <p class="service-text">Sed ut perspiciatis &nbsp;accusantium doloremque ulla laboris laudantium</p>
    <a class="read-more">Read More <svg width="14" height="14" viewBox="0 0 16 16"><circle cx="8" cy="8" r="8" fill="var(--blue)"/><path d="M6 4l4 4-4 4" fill="none" stroke="#fff" stroke-width="2.2"/></svg></a>
  </article>

  <article class="service-card" style="left:457px">
    <div class="service-photo" role="img" aria-label="Photo of a desk with a laptop, law book and scales" style="background:linear-gradient(135deg,#8a8880,#2e2a26)"></div>
    <span class="service-badge"><svg width="26" height="26" viewBox="0 0 26 26"><rect x="3" y="8" width="20" height="13" rx="2" fill="none" stroke="#fff" stroke-width="2"/><path d="M9 8V5h8v3" fill="none" stroke="#fff" stroke-width="2"/></svg></span>
    <h3 class="service-name">LOREM IPSUM DOLOR SIT</h3>
    <p class="service-text">Sed ut perspiciatis &nbsp;accusantium doloremque ulla laboris laudantium</p>
    <a class="read-more">Read More <svg width="14" height="14" viewBox="0 0 16 16"><circle cx="8" cy="8" r="8" fill="var(--blue)"/><path d="M6 4l4 4-4 4" fill="none" stroke="#fff" stroke-width="2.2"/></svg></a>
  </article>

  <article class="service-card" style="left:774px">
    <div class="service-photo" role="img" aria-label="Photo of a police officer at a crowded street event" style="background:linear-gradient(135deg,#6c6a78,#1c2030)"></div>
    <span class="service-badge"><svg width="26" height="26" viewBox="0 0 26 26"><rect x="5" y="10" width="16" height="11" fill="none" stroke="#fff" stroke-width="2"/><path d="M3 10l10-6 10 6" fill="none" stroke="#fff" stroke-width="2"/></svg></span>
    <h3 class="service-name">LOREM IPSUM DOLOR SIT</h3>
    <p class="service-text">Sed ut perspiciatis &nbsp;accusantium doloremque ulla laboris laudantium</p>
    <a class="read-more">Read More <svg width="14" height="14" viewBox="0 0 16 16"><circle cx="8" cy="8" r="8" fill="var(--blue)"/><path d="M6 4l4 4-4 4" fill="none" stroke="#fff" stroke-width="2.2"/></svg></a>
  </article>
</section>

<section class="blogs">
  <h2 class="section-title" style="top:1911px">LATEST BLOGS</h2>
  <div class="blog-photo" role="img" aria-label="Photo of an officer briefing staff in an office" style="left:127px;background:linear-gradient(135deg,#e8e4de,#8c7a68)"></div>
  <div class="blog-photo" role="img" aria-label="Photo of a team working at computer monitors" style="left:621px;background:linear-gradient(135deg,#d6dbe0,#6b5a52)"></div>

  <article class="blog-card" style="left:153px">
    <h3 class="blog-name">LOREM DOLOR CONSECTETUR ADIPISCING</h3>
    <p class="blog-meta"><b>Nov 9.11.2021</b>| Lorem ipsum dolor sit amet,</p>
    <p class="blog-text">Sed ut perspiciatis unde omnis iste natus error sit voluptatem accusantium doloremque laudantium, totam rem aperiam, eaque ipsa quae inventore</p>
  </article>
  <article class="blog-card" style="left:656px">
    <h3 class="blog-name">LOREM DOLOR CONSECTETUR ADIPISCING</h3>
    <p class="blog-meta"><b>Nov 9.11.2021</b>| Lorem ipsum dolor sit amet,</p>
    <p class="blog-text">Sed ut perspiciatis unde omnis iste natus error sit voluptatem accusantium doloremque laudantium, totam rem aperiam, eaque ipsa quae inventore</p>
  </article>
</section>

<section class="contact">
  <div class="contact-band"></div>
  <h2 class="section-title light" style="top:2561px">GET IN TOUCH</h2>
  <div class="field" style="left:222px;top:2656px;width:375px;height:35px">Name:</div>
  <div class="field" style="left:611px;top:2656px;width:365px;height:35px">Email:</div>
  <div class="field" style="left:222px;top:2710px;width:375px;height:35px">Address:</div>
  <div class="field" style="left:611px;top:2710px;width:366px;height:35px">Phone:</div>
  <div class="field" style="left:222px;top:2763px;width:755px;height:74px">Massage:</div>
  <a class="btn-submit">SUBMIT
    <svg width="15" height="15" viewBox="0 0 16 16"><circle cx="8" cy="8" r="8" fill="#fff"/><path d="M4 8l8-3-3 8-1-4z" fill="var(--blue)"/></svg>
  </a>
</section>

<footer class="site-footer">
  <svg class="abs" style="left:0;top:0" width="1200" height="455" viewBox="0 0 1200 455">
    <path d="M0 70L600 3L1200 70V455H0Z" fill="var(--footer)"/>
    <path d="M0 70L600 3L1200 70" fill="none" stroke="#fff" stroke-width="4"/>
  </svg>
</footer>
<div class="footer-brand"><span class="brand-dot"></span><span class="brand-name">BASTION</span></div>
<p class="footer-about">Sed ut perspiciatis unde omnis iste natus error voluptatem accusantium</p>
<h4 class="footer-head" style="left:111px;top:3271px">Follow Us</h4>
<span class="social" role="img" aria-label="Social link" style="left:110px"></span>
<span class="social" role="img" aria-label="Social link" style="left:151px"></span>
<span class="social" role="img" aria-label="Social link" style="left:193px"></span>
<span class="social" role="img" aria-label="Social link" style="left:233px"></span>

<h4 class="footer-head" style="left:468px;top:3106px">Quicklinks</h4>
<a class="footer-link" style="left:468px;top:3165px">Home</a>
<a class="footer-link" style="left:468px;top:3199px">About Us</a>
<a class="footer-link" style="left:468px;top:3233px">Services</a>
<a class="footer-link" style="left:468px;top:3267px">Blog</a>
<a class="footer-link" style="left:468px;top:3301px">Contact Us</a>

<h4 class="footer-head" style="left:673px;top:3106px">Otherlinks</h4>
<a class="footer-link" style="left:673px;top:3165px">FAQ</a>
<a class="footer-link" style="left:673px;top:3203px">Services</a>
<a class="footer-link" style="left:673px;top:3242px">Team</a>
<a class="footer-link" style="left:673px;top:3280px">Privacy</a>
<a class="footer-link" style="left:673px;top:3319px">Policy</a>

<h4 class="footer-head" style="left:881px;top:3106px">Contact Us</h4>
<span class="contact-icon" style="top:3171px"><svg width="16" height="16" viewBox="0 0 16 16"><path d="M3 1l3 3-2 2c1 2 3 4 5 5l2-2 3 3-2 3C7 15 1 9 1 3z" fill="var(--blue)"/></svg></span>
<span class="contact-label" style="top:3169px">Phone Number</span>
<span class="contact-value" style="top:3189px">555-0142-800</span>
<span class="contact-icon" style="top:3239px"><svg width="16" height="12" viewBox="0 0 16 12"><rect x="1" y="1" width="14" height="10" fill="none" stroke="var(--blue)" stroke-width="1.6"/><path d="M1 1l7 6 7-6" fill="none" stroke="var(--blue)" stroke-width="1.6"/></svg></span>
<span class="contact-label" style="top:3236px">Email:</span>
<span class="contact-value" style="top:3257px">info@bastion-support.com</span>
<span class="contact-icon" style="top:3292px"><svg width="14" height="18" viewBox="0 0 14 18"><path d="M7 1a6 6 0 0 1 6 6c0 4-6 10-6 10S1 11 1 7a6 6 0 0 1 6-6z" fill="var(--blue)"/><circle cx="7" cy="7" r="2.2" fill="#fff"/></svg></span>
<span class="contact-label" style="top:3305px">Address :</span>
<span class="contact-value" style="top:3325px">Lorem ipsum dolor amet<br>consectetur adipiscing</span>

<div class="footer-rule"></div>
<p class="copyright">© 2021 Bastion &nbsp;| All right reserved &nbsp;|</p>

</body>
</html>
```